Flyer Design Project

We would like a double sided a5 flyer. To promote our new brand which is velvetine mobile, attached is the logo. This is for a mobile telecom company.
The aim of the flyer is to create brand awareness, to pormote a managed service for mobile phone connections/ tariffs. For business users and also personal use.

We would like to focus to be on offshore billing and discrete billing for users based abroad. eg students

Theme should be based around Plumleaf and Zorphones , one side should focus on business users and the other should focus on personal use. The focus on business users should be based around , Virtual landline numbers, where users can have a landline number connected to their mobile phones.
Should be elegant, up class ,and not to much text bullet points would be good .

Branding of telecoms QX ,K7 ,Telmarix,.
Updates

Velvetine mobile

Contact info for the flyer. 
info@velvetinemobile.example
www.velvetinemobile.example
0871 463 19 19 

Flyers need to look elegant and good creative designs please.

Industry/Entity Type

Telecom

```html
<!DOCTYPE html>
<html lang="en">
<head>
<meta charset="utf-8">
<title>Velvetine mobile flyer</title>
<link rel="stylesheet" href="https://fonts.googleapis.com/css2?family=Didact+Gothic&display=swap">
<style>
  :root {
    --page-bg: #8c8c8c;
    --flyer-bg: #0b0b0b;
    --flyer-glow: #1c1c1c;
    --text: #f2f2f2;
    --text-soft: #c9c9c9;
    --band-business: #1aa3dc;
    --band-personal: #7cc242;
    --accent-dot: #7cc242;
    --device-dark: #1a1a1a;
    --device-mid: #3a3f46;
    --device-light: #6e7680;
    --screen-green: #5f9e2c;
  }
  * { box-sizing: border-box; margin: 0; padding: 0; }
  html, body { width: 1200px; height: 900px; overflow: hidden; }
  body {
    background: var(--page-bg);
    font-family: "Didact Gothic", "Century Gothic", sans-serif;
    color: var(--text);
  }
  .flyer {
    position: absolute;
    left: 310px; top: 40px;
    width: 580px; height: 820px;
    overflow: hidden;
    background: radial-gradient(ellipse at 55% 40%, var(--flyer-glow) 0%, var(--flyer-bg) 65%);
    box-shadow: 0 10px 30px rgba(0,0,0,.35);
  }
  .brand {
    position: absolute; left: 34px; top: 30px;
    display: flex; align-items: center; gap: 10px;
  }
  .brand-mark {
    width: 14px; height: 14px; border-radius: 50%;
    background: var(--accent-dot);
  }
  .brand-name {
    font-size: 19px; font-weight: 400; letter-spacing: 1.5px; text-transform: uppercase;
    color: var(--text);
  }
  .hero-devices {
    position: absolute; left: 250px; top: 90px;
    width: 310px; height: 170px; border-radius: 12px;
    background: linear-gradient(90deg, var(--device-mid), var(--device-dark) 45%, var(--device-mid) 70%, var(--device-dark));
  }
  .band {
    position: absolute; left: 0; height: 34px;
    display: flex; align-items: center; padding-left: 34px;
    font-size: 24px; font-weight: 400; letter-spacing: .5px; color: var(--text);
    border-radius: 0 6px 6px 0;
  }
  .band-business { top: 210px; width: 330px; background: var(--band-business); }
  .band-personal { top: 405px; width: 320px; background: var(--band-personal); }
  .points {
    position: absolute; left: 34px; width: 500px;
    list-style: none; font-size: 16px; line-height: 1.35; color: var(--text);
  }
  .points li { position: relative; padding-left: 18px; }
  .points li::before {
    content: ""; position: absolute; left: 0; top: 6px;
    width: 9px; height: 9px; background: var(--text-soft);
  }
  .points-business { top: 255px; }
  .points-personal { top: 450px; }
  .handsets {
    position: absolute; left: 30px; top: 560px;
    width: 240px; height: 200px; border-radius: 14px;
    background: linear-gradient(120deg, var(--device-light) 0%, var(--device-mid) 35%, var(--device-dark) 60%, var(--screen-green) 85%);
  }
  .contact {
    position: absolute; left: 300px; top: 590px;
    width: 260px;
    border-left: 2px solid var(--text-soft);
    padding-left: 16px;
    list-style: none; font-size: 14px; line-height: 1.5;
  }
  .contact li { display: flex; align-items: flex-start; gap: 9px; white-space: nowrap; }
  .contact svg { width: 13px; height: 13px; flex: none; margin-top: 4px; fill: var(--text); }
  .contact .web { font-size: 15px; }
</style>
</head>
<body>
  <main class="flyer">
    <header class="brand">
      <span class="brand-mark"></span>
      <span class="brand-name">Velvetine mobile</span>
    </header>

    <div class="hero-devices" role="img" aria-label="Row of touchscreen smartphones showing maps, news and app screens"></div>

    <h2 class="band band-business">Business Usage</h2>
    <ul class="points points-business">
      <li>Never miss a business call again!</li>
      <li>The complete telephone system solution for small businesses.</li>
      <li>With an impressive range of professional call handling features, LinkOne Express allows small businesses to be responsive 24/7 by combining your landline and mobile calls.</li>
    </ul>

    <h2 class="band band-personal">Personal Usage</h2>
    <ul class="points points-personal">
      <li>Never miss a call again, get your landline number on your mobile.</li>
      <li>Offshore and discrete billing</li>
      <li>We will save you money of your existing mobile provider.</li>
    </ul>

    <div class="handsets" role="img" aria-label="Three keyboard and touchscreen handsets with reflections"></div>

    <ul class="contact">
      <li>
        <svg viewBox="0 0 16 16"><path d="M8 1 1 7.5h2V15h4v-4h2v4h4V7.5h2z"/></svg>
        <span>48 Harrow Lane, Elmfield<br>SA 5100</span>
      </li>
      <li>
        <svg viewBox="0 0 16 16"><path d="M5 1h6a1 1 0 0 1 1 1v12a1 1 0 0 1-1 1H5a1 1 0 0 1-1-1V2a1 1 0 0 1 1-1zm0 2v9h6V3z"/></svg>
        <span>0871 463 19 19</span>
      </li>
      <li>
        <svg viewBox="0 0 16 16"><path d="M4 1l2 3.5-1.5 1.5a9 9 0 0 0 5.5 5.5L11.5 10 15 12l-1 3C7 15 1 9 1 2z"/></svg>
        <span>0871 463 19 19</span>
      </li>
      <li>
        <svg viewBox="0 0 16 16"><path d="M1 3h14v10H1zm1.5 1.3v.4L8 9l5.5-4.3v-.4z"/></svg>
        <span>info@velvetinemobile.example</span>
      </li>
      <li class="web">
        <svg viewBox="0 0 16 16"><circle cx="8" cy="8" r="7"/></svg>
        <span>www.velvetinemobile.example</span>
      </li>
    </ul>
  </main>
</body>
</html>
```